St Louis Electrician Needing a Business Card Design!!

We are a St Louis based electrical contracting firm that needs help designing a business card. We have a logo and I have another image that I would like to incorporate. Open to ideas..Thanks!!

Industry/Entity Type

Business

Requirements
Must have
• there are two downloads...one is the logo and the other is what i was wanting coming off the logo...the light rays. Like the logo with the blue background...Was thinking the whole card would be that color blue.
Should not have
• No lightning bolts

```html
<!DOCTYPE html>
<html lang="en">
<head>
<meta charset="utf-8">
<title>Quellbright Electric Inc. – Business Card</title>
<link rel="stylesheet" href="https://fonts.googleapis.com/css2?family=Open+Sans:wght@400;700&display=swap">
<style>
  :root {
    --backdrop: #2c2e33;
    --card-blue: #0b56a6;
    --card-blue-panel: #0e5bab;
    --ink-white: #ffffff;
    --card-shadow: rgba(0, 0, 0, 0.45);
  }
  * { box-sizing: border-box; margin: 0; padding: 0; }
  html, body {
    width: 1200px;
    height: 864px;
    overflow: hidden;
    background: var(--backdrop);
    font-family: "Open Sans", sans-serif;
    color: var(--ink-white);
  }
  .sheet {
    position: relative;
    width: 1200px;
    height: 864px;
    display: flex;
    align-items: center;
    justify-content: center;
    gap: 40px;
  }
  .card {
    position: relative;
    width: 540px;
    height: 309px;
    background: var(--card-blue);
    box-shadow: 0 14px 30px var(--card-shadow);
    overflow: hidden;
  }
  .card__panel {
    position: absolute;
    background: var(--card-blue-panel);
  }
  .card--front .card__panel { left: 62px; top: 46px; width: 416px; height: 217px; }
  .card--back .card__panel { left: 250px; top: 0; width: 290px; height: 196px; }

  .wordmark {
    position: absolute;
    font-weight: 400;
    color: var(--ink-white);
    line-height: 1;
    white-space: nowrap;
  }
  .wordmark__name { display: block; }
  .wordmark__suffix { display: block; text-align: right; }

  .card--front .wordmark { left: 100px; top: 112px; }
  .card--front .wordmark__name { font-size: 34px; }
  .card--front .wordmark__suffix { font-size: 15px; margin-top: 4px; }

  .card--back .wordmark { right: 40px; top: 68px; }
  .card--back .wordmark__name { font-size: 27px; }
  .card--back .wordmark__suffix { font-size: 12px; margin-top: 3px; }

  .person {
    position: absolute;
    left: 40px;
    top: 146px;
  }
  .person__name { font-size: 19px; font-weight: 700; line-height: 1.2; }
  .person__role { font-size: 13px; font-weight: 400; line-height: 1.3; }

  .contact {
    position: absolute;
    right: 26px;
    bottom: 14px;
    list-style: none;
    text-align: right;
    font-size: 14px;
    line-height: 21px;
  }
  .contact__item {
    display: flex;
    justify-content: flex-end;
    align-items: center;
    gap: 10px;
    white-space: nowrap;
  }
  .contact__icon { width: 12px; height: 12px; fill: var(--ink-white); flex: none; }
  .contact__item--address { margin-right: -8px; }
</style>
</head>
<body>
<main class="sheet">

  <section class="card card--front" aria-label="Card front">
    <div class="card__panel"></div>
    <div class="wordmark">
      <span class="wordmark__name">Quellbright Electric</span>
      <span class="wordmark__suffix">Inc.</span>
    </div>
  </section>

  <section class="card card--back" aria-label="Card back">
    <div class="card__panel"></div>
    <div class="wordmark">
      <span class="wordmark__name">Quellbright Electric</span>
      <span class="wordmark__suffix">Inc.</span>
    </div>

    <div class="person">
      <p class="person__name">Orrin Vantelli</p>
      <p class="person__role">Managing Director</p>
    </div>

    <ul class="contact">
      <li class="contact__item">
        <span>(000)-555-0190</span>
        <svg class="contact__icon" viewBox="0 0 24 24" aria-hidden="true"><path d="M6.6 10.8a15.1 15.1 0 0 0 6.6 6.6l2.2-2.2a1 1 0 0 1 1-.25 11.4 11.4 0 0 0 3.6.57 1 1 0 0 1 1 1V20a1 1 0 0 1-1 1A17 17 0 0 1 3 4a1 1 0 0 1 1-1h3.5a1 1 0 0 1 1 1c0 1.25.2 2.45.57 3.57a1 1 0 0 1-.25 1z"/></svg>
      </li>
      <li class="contact__item">
        <span>info@quellbright.example</span>
        <svg class="contact__icon" viewBox="0 0 24 24" aria-hidden="true"><path d="M2 5h20v14H2z M3.5 6.5 12 13l8.5-6.5" fill="none" stroke="#fff" stroke-width="2"/><path d="M2 5h20L12 12.5z"/></svg>
      </li>
      <li class="contact__item">
        <span>www.quellbright.example</span>
        <svg class="contact__icon" viewBox="0 0 24 24" aria-hidden="true"><path d="M10 14a4 4 0 0 0 5.7 0l3.6-3.6a4 4 0 0 0-5.7-5.7L12 6.3M14 10a4 4 0 0 0-5.7 0l-3.6 3.6a4 4 0 0 0 5.7 5.7L12 17.7" fill="none" stroke="#fff" stroke-width="2.4" stroke-linecap="round"/></svg>
      </li>
      <li class="contact__item contact__item--address">
        <span>12345, Lumen Row Example City Name, 000000</span>
      </li>
    </ul>
  </section>

</main>
</body>
</html>
```